Modern Dental Appointment Reminder/Business Card

We already have a beautiful logo and icon picked from here on PixelHarbor, now we need someone to make them into a beautiful business card for us! This business card will also function as an appointment reminder card for patients. It will be double sided and must include:
Front
-Contact Info as Follows:
(Gavin T Morrow, DDS
Family and Cosmetic Dentistry
2947 S 3260 E Ste 400
Farmington, Utah 84093)
-Our Logo or Icon (your choice, if Icon must write "Bluefern Dental" below it like in the example file)
Back
-"You're Invited!"
-"Your next appointment is on"
-Place to write date & time
-"Please call 24hrs ahead if appointment is to be cancelled
-Our Icon

Logo and Icon to be used are attached below, along with an example of what we need.
Please do NOT use lots of red! We want the red to just be an accent. Please use grey, white, or even a muted teal for the majority of the card.

Industry/Entity Type

Dentistry

Contact Information for Business Card

Gavin T Morrow, DDS
2947 S 3260 E Ste 400
Farmington, Utah 84093

Colors
cfeae6

Requirements
Should not have
• Lots of red!

```html
<!DOCTYPE html>
<html lang="en">
<head>
<meta charset="utf-8">
<title>Bluefern Dental – Business and Appointment Card</title>
<link href="https://fonts.googleapis.com/css2?family=Crimson+Text:ital,wght@0,400;1,400&family=Merienda:wght@400&display=swap" rel="stylesheet">
<style>
  :root {
    --backdrop: #2b2b2d;
    --card-teal: #cfeae6;
    --card-glow: #f4fbfa;
    --ink-grey: #57524c;
    --accent-red: #a52a2a;
    --field-white: #ffffff;
  }
  * { margin: 0; padding: 0; box-sizing: border-box; }
  html, body {
    width: 1200px; height: 900px; overflow: hidden;
    background: var(--backdrop);
    font-family: "Crimson Text", Georgia, serif;
    color: var(--ink-grey);
  }
  .sheet {
    width: 1200px; height: 900px;
    display: flex; flex-direction: column; align-items: center; justify-content: center;
    gap: 22px;
  }
  .card {
    position: relative;
    width: 720px; height: 411px;
    background: var(--card-teal);
    overflow: hidden;
  }
  /* Front */
  .card--front {
    background: radial-gradient(circle at 62% 58%, var(--card-glow) 0%, var(--card-teal) 45%);
  }
  .brand {
    position: absolute; left: 60px; top: 56px; width: 300px;
    display: flex; flex-direction: column; align-items: center; gap: 16px;
  }
  .brand__dot {
    width: 96px; height: 96px; border-radius: 50%;
    background: var(--ink-grey);
  }
  .brand__name {
    font-size: 30px; font-variant: small-caps; letter-spacing: 2px;
    color: var(--ink-grey); white-space: nowrap;
  }
  .dentist {
    position: absolute; right: 56px; top: 118px; text-align: right;
  }
  .dentist__name { font-size: 25px; line-height: 30px; color: var(--ink-grey); }
  .dentist__title { font-size: 17px; line-height: 22px; color: var(--accent-red); }
  .contact {
    position: absolute; left: 300px; top: 250px;
    display: flex; gap: 12px;
  }
  .contact__icons {
    display: flex; flex-direction: column; gap: 8px; padding-top: 4px;
    border-right: 1px solid var(--ink-grey); padding-right: 10px;
  }
  .contact__icons svg { width: 14px; height: 14px; fill: var(--accent-red); }
  .contact__lines { font-size: 17px; line-height: 22px; white-space: nowrap; }
  /* Back */
  .invite {
    position: absolute; left: 46px; top: 44px; width: 400px;
  }
  .invite__heading {
    font-family: "Merienda", cursive;
    font-size: 34px; color: var(--ink-grey);
  }
  .invite__lead { font-size: 17px; margin-top: 2px; margin-bottom: 14px; }
  .field {
    display: flex; align-items: center; justify-content: space-between;
    background: var(--field-white); border-radius: 20px;
    height: 32px; padding: 0 18px; margin-bottom: 10px;
    font-size: 15px;
  }
  .field__label { width: 60px; }
  .invite__note { font-size: 16px; font-style: italic; margin-top: 18px; }
  .back-mark {
    position: absolute; right: -70px; top: 70px;
    width: 330px; height: 330px; border-radius: 50%;
    background: var(--ink-grey);
    display: flex; align-items: center; justify-content: flex-start;
    padding-left: 30px;
  }
  .back-mark__name {
    font-size: 24px; font-variant: small-caps; letter-spacing: 1px;
    color: var(--card-teal); white-space: nowrap;
  }
</style>
</head>
<body>
<main class="sheet">
  <section class="card card--front" aria-label="Card front">
    <div class="brand">
      <span class="brand__dot"></span>
      <span class="brand__name">Bluefern Dental</span>
    </div>
    <div class="dentist">
      <p class="dentist__name">Gavin T Morrow, DDS</p>
      <p class="dentist__title">Family and Cosmetic Dentistry</p>
    </div>
    <div class="contact">
      <div class="contact__icons">
        <svg viewBox="0 0 24 24" aria-label="Phone"><path d="M6.6 10.8a15 15 0 0 0 6.6 6.6l2.2-2.2a1 1 0 0 1 1-.25 11.4 11.4 0 0 0 3.6.57 1 1 0 0 1 1 1V20a1 1 0 0 1-1 1A17 17 0 0 1 3 4a1 1 0 0 1 1-1h3.5a1 1 0 0 1 1 1c0 1.25.2 2.45.57 3.57a1 1 0 0 1-.25 1z"/></svg>
        <svg viewBox="0 0 24 24" aria-label="Fax"><path d="M6 2h12v6H6zM3 9h18a1 1 0 0 1 1 1v7h-4v5H6v-5H2v-7a1 1 0 0 1 1-1zm5 8v3h8v-3z"/></svg>
        <svg viewBox="0 0 24 24" aria-label="Address"><path d="M12 2a7 7 0 0 0-7 7c0 5 7 13 7 13s7-8 7-13a7 7 0 0 0-7-7zm0 9.5A2.5 2.5 0 1 1 12 6.5a2.5 2.5 0 0 1 0 5z"/></svg>
      </div>
      <div class="contact__lines">
        <p>775.555.0142</p>
        <p>775.555.0187</p>
        <p>2947 S 3260 E Ste 400</p>
        <p>Larkspur Falls, Nevada 89504</p>
      </div>
    </div>
  </section>

  <section class="card card--back" aria-label="Card back">
    <div class="invite">
      <h1 class="invite__heading">You're Invited!</h1>
      <p class="invite__lead">Your next appointment is on:</p>
      <div class="field"><span class="field__label">Time</span><span>:</span><span>AM / PM</span></div>
      <div class="field"><span class="field__label">Date</span><span>/</span><span>/</span><span></span></div>
      <p class="invite__note">Please call 24hrs ahead if appointment is to be cancelled</p>
    </div>
    <div class="back-mark">
      <span class="back-mark__name">Bluefern Dental</span>
    </div>
  </section>
</main>
</body>
</html>
```